Stationery Design needed for logo design project

This project is linked to Logo: brand identity for modern furniture design studio..

Our company needs a Stationery Design. Please refer to our original project in the link above.

```html
<!DOCTYPE html>
<html lang="en">
<head>
<meta charset="utf-8">
<title>halden stationery</title>
<link rel="stylesheet" href="https://fonts.googleapis.com/css2?family=Carlito:wght@400&family=Lato:wght@300&family=Caveat:wght@400&display=swap">
<style>
  :root{
    --backdrop:#c6c6c6;
    --paper:#ffffff;
    --ink:#2b2b2b;
    --body-ink:#3a3a3a;
    --band-dark:#3f3f3f;
    --band-mid:#8a8a8a;
    --rule:#555555;
  }
  *{margin:0;padding:0;box-sizing:border-box}
  html,body{width:1200px;height:751px;overflow:hidden;background:var(--backdrop)}
  body{position:relative;font-family:"Carlito",sans-serif;color:var(--ink)}
  .sheet{position:absolute;background:var(--paper);box-shadow:0 1px 4px rgba(0,0,0,.25)}

  /* Letterhead */
  .letterhead{left:47px;top:25px;width:542px;height:710px}
  .letterhead .spine{position:absolute;left:12px;width:7px;background:var(--band-dark)}
  .spine.main{top:0;height:580px}
  .spine.block-a{top:590px;height:40px}
  .spine.block-b{top:640px;height:50px;background:var(--band-mid)}
  .spine.block-c{top:697px;height:13px}
  .wordmark{font-family:"Lato",sans-serif;font-weight:300;color:var(--ink);letter-spacing:1px;line-height:1}
  .letterhead .wordmark{position:absolute;left:0;right:0;top:38px;text-align:center;font-size:62px}
  .letterhead .mark-rule{position:absolute;left:198px;width:145px;top:101px;height:2px;background:linear-gradient(90deg,transparent,#ddd,transparent)}
  .letter-body{position:absolute;left:25px;width:489px;top:192px;height:290px;overflow:hidden;font-size:10.7px;line-height:19.2px;text-align:justify;color:var(--body-ink)}
  .letter-body p{text-indent:15px;margin-bottom:19.2px}
  .sign-off{position:absolute;left:392px;width:100px;top:496px;text-align:center;font-size:10.5px;line-height:14px;color:var(--body-ink)}
  .sign-off .signature{font-family:"Caveat",cursive;font-size:14px;color:#777;margin:6px 0 4px;display:block;transform:skewX(-8deg)}
  .letter-contact{position:absolute;top:632px;font-size:7.8px;line-height:9px;color:var(--body-ink)}
  .letter-contact li{list-style:none;display:flex;gap:7px;margin-bottom:8px;align-items:flex-start}
  .letter-contact svg{width:9px;height:9px;flex:none}
  .contact-left{left:62px}
  .contact-right{left:163px}

  /* Window envelope */
  .envelope-front{left:606px;top:27px;width:544px;height:256px}
  .envelope-front .wordmark{position:absolute;left:33px;top:30px;font-size:52px}
  .envelope-front .mark-rule{position:absolute;left:50px;width:130px;top:83px;height:2px;background:linear-gradient(90deg,transparent,#ddd,transparent)}
  .address-window{position:absolute;left:35px;top:118px;width:206px;height:65px;border:1px solid #666;border-radius:10px;background:linear-gradient(160deg,#fff 40%,#f1f1f1)}
  .contact-row{position:absolute;left:22px;right:20px;top:218px;display:flex;align-items:center;gap:12px;font-size:7.2px;color:var(--body-ink)}
  .contact-row span{display:flex;align-items:center;gap:5px;padding-left:8px;border-left:1px solid var(--rule)}
  .contact-row svg{width:8px;height:8px}
  .base-band{position:absolute;left:0;right:0;bottom:0;height:13px;background:var(--band-dark)}

  /* Envelope back */
  .envelope-back{left:606px;top:349px;width:544px;height:256px}
  .envelope-back .flap{position:absolute;left:0;top:0;width:544px;height:72px}
  .envelope-back .wordmark{position:absolute;left:0;right:0;top:20px;text-align:center;font-size:28px}
  .envelope-back .base-band{height:8px}
</style>
</head>
<body>

<section class="sheet letterhead">
  <div class="spine main"></div>
  <div class="spine block-a"></div>
  <div class="spine block-b"></div>
  <div class="spine block-c"></div>

  <h1 class="wordmark">halden</h1>
  <div class="mark-rule"></div>

  <div class="letter-body">
    <p>Lorem ipsum dolor sit amet, consectetuer adipiscing elit. Aenean commodo ligula eget dolor. Aenean massa. Cum sociis natoque penatibus et magnis dis parturient montes, nascetur ridiculus mus. Donec quam felis, ultricies nec, pellentesque eu, pretium quis, sem. Nulla consequat massa quis enim. Donec pede justo, fringilla vel, aliquet nec, vulputate eget, arcu. In enim justo, rhoncus ut, imperdiet a, venenatis vitae, justo. Nullam dictum felis eu pede mollis pretium. Integer tincidunt. Cras dapibus. Vivamus elementum semper nisi.</p>
    <p>Integer tincidunt. Cras dapibus. Vivamus elementum semper nisi. Aenean vulputate eleifend tellus. Aenean leo ligula, porttitor eu, consequat vitae, eleifend ac, enim. Aliquam lorem ante, dapibus in, viverra quis, feugiat a, tellus. Phasellus viverra nulla ut metus varius laoreet. Quisque rutrum. Aenean imperdiet. Etiam ultricies nisi vel augue. Curabitur ullamcorper ultricies nisi. Nam eget dui. Etiam rhoncus. Maecenas tempus, tellus eget condimentum rhoncus, sem quam semper libero, sit amet adipiscing sem neque sed ipsum. Nam quam nunc, blandit vel, luctus pulvinar, hendrerit id, lorem. Maecenas nec odio et ante tincidunt tempus. Donec vitae sapien ut libero venenatis faucibus. Nullam quis ante. Etiam sit amet orci eget eros faucibus tincidunt. Duis leo. Sed fringilla mauris sit amet nibh. Donec sodales sagittis magna. Sed consequat, leo eget bibendum sodales, augue velit cursus nunc, Vestibulum volutpat pretium libero. Cras id dui. Aenean ut</p>
  </div>

  <div class="sign-off">
    yours sincerely
    <span class="signature">John Doe</span>
    JOHN DOE
  </div>

  <ul class="letter-contact contact-left">
    <li><svg viewBox="0 0 10 10"><path d="M2 1l2 2-1 1.2c.6 1.3 1.5 2.2 2.8 2.8L7 6l2 2-1.2 1.2C4.5 9 1 5.5.8 2.2z" fill="#333"/></svg>555-210-4830</li>
    <li><svg viewBox="0 0 10 10"><path d="M5 .5a3.3 3.3 0 0 0-3.3 3.3C1.7 6.3 5 9.5 5 9.5s3.3-3.2 3.3-5.7A3.3 3.3 0 0 0 5 .5zm0 4.7a1.4 1.4 0 1 1 0-2.8 1.4 1.4 0 0 1 0 2.8z" fill="#333"/></svg><span>418 Linden Court<br>Bay Area<br>CA-75021</span></li>
  </ul>
  <ul class="letter-contact contact-right">
    <li><svg viewBox="0 0 10 10"><rect x=".8" y="2" width="8.4" height="6" fill="none" stroke="#333"/><path d="M.8 2L5 5.5 9.2 2" fill="none" stroke="#333"/></svg>info@halden.com</li>
    <li><svg viewBox="0 0 10 10"><circle cx="5" cy="5" r="4.3" fill="#333"/><path d="M.7 5h8.6M5 .7c-2 2.5-2 6.1 0 8.6M5 .7c2 2.5 2 6.1 0 8.6" fill="none" stroke="#fff" stroke-width=".6"/></svg>www.halden.com</li>
  </ul>
</section>

<section class="sheet envelope-front">
  <h2 class="wordmark">halden</h2>
  <div class="mark-rule"></div>
  <div class="address-window"></div>
  <div class="contact-row">
    <span><svg viewBox="0 0 10 10"><path d="M2 1l2 2-1 1.2c.6 1.3 1.5 2.2 2.8 2.8L7 6l2 2-1.2 1.2C4.5 9 1 5.5.8 2.2z" fill="#333"/></svg>555-210-4830</span>
    <span><svg viewBox="0 0 10 10"><path d="M5 .5a3.3 3.3 0 0 0-3.3 3.3C1.7 6.3 5 9.5 5 9.5s3.3-3.2 3.3-5.7A3.3 3.3 0 0 0 5 .5zm0 4.7a1.4 1.4 0 1 1 0-2.8 1.4 1.4 0 0 1 0 2.8z" fill="#333"/></svg>418 Linden Court&nbsp; Bay Area&nbsp; CA-75021</span>
    <span><svg viewBox="0 0 10 10"><rect x=".8" y="2" width="8.4" height="6" fill="none" stroke="#333"/><path d="M.8 2L5 5.5 9.2 2" fill="none" stroke="#333"/></svg>info@halden.com</span>
    <span><svg viewBox="0 0 10 10"><circle cx="5" cy="5" r="4.3" fill="#333"/><path d="M.7 5h8.6M5 .7c-2 2.5-2 6.1 0 8.6M5 .7c2 2.5 2 6.1 0 8.6" fill="none" stroke="#fff" stroke-width=".6"/></svg>www.halden.com</span>
  </div>
  <div class="base-band"></div>
</section>

<section class="sheet envelope-back">
  <svg class="flap" viewBox="0 0 544 72" aria-hidden="true">
    <polygon points="0,0 544,0 528,68 16,68" fill="#fdfdfd" stroke="#d4d4d4" stroke-width="1"/>
    <line x1="16" y1="69" x2="528" y2="69" stroke="#e6e6e6" stroke-width="3"/>
  </svg>
  <h2 class="wordmark">halden</h2>
  <div class="base-band"></div>
</section>

</body>
</html>
```